Bright Haven Estate Sales web design

We are looking to launch an Estate Sales Website for Nashville, TN. The name of our Business is Bright Haven Estate Sales. We would like to give you a blank slate so that you can showcase your design skills for us. The few things we are looking for are a nice header graphic of a house or a stock image of an estate sale. Near the header graphic we would like a quick inquiry form. If not on the right side of the header maybe midway down the site. We potentially want to see what purple and Gold look like on the site however this is not a must. We have over 20 years of industry related experience.

1. Buttons at top of the website will be.
a. Services
b. Upcoming Sales
c. About Us
d. FAQs
e. Resources

Services we offer:
1. Estate Sales
2. Cleanouts
3. Appraisals

Sites We like:
https://www.corvellestatesales.example/

We don't have a logo yet so if you have ideas please share them with us. Below are 2 ideas however if you have your own thoughts please ignore.

1. Oval ornate frame, gold and black, with BHES in the middle, deep purple. Think of catering to high class people..font should be fancy as opposed to simple.

2. Another option, Bright Haven in bold fancy script, same colors, with Estate Sales below, small different font, black.

```html
<!DOCTYPE html>
<html lang="en">
<head>
<meta charset="utf-8">
<title>Bright Haven Estate Sales</title>
<link rel="stylesheet" href="https://fonts.googleapis.com/css2?family=Poppins:wght@400;500;600;700;800&family=Oswald:wght@400;600&display=swap">
<style>
:root{
  --purple:#5a27a5;
  --purple-deep:#4a1f8c;
  --gold:#c9962e;
  --dark:#333333;
  --panel:#2e2e2e;
  --white:#ffffff;
  --ink:#2b2b2b;
  --grey:#6b6b6b;
}
*{box-sizing:border-box;margin:0;padding:0}
html,body{width:1200px;height:4387px;overflow:hidden}
body{position:relative;background:var(--white);font-family:"Poppins",sans-serif;color:var(--ink)}
.abs{position:absolute}
svg.band{position:absolute;left:0;width:1200px;display:block}

/* hero */
.hero-photo{left:0;top:0;width:1200px;height:820px;background:linear-gradient(180deg,#203a5c 0%,#3d5b44 30%,#6b7d8a 50%,#5f8a3a 72%,#4b7a2a 100%)}
.hero-panel{left:0;top:135px;width:683px;height:680px;background:rgba(90,39,165,.85);border-bottom-right-radius:90% 60%}
.site-nav{left:0;top:0;width:1200px;height:110px}
.brand{left:40px;top:28px;display:flex;align-items:center;gap:10px}
.brand-mark{width:36px;height:36px;border-radius:50%;border:3px solid var(--gold)}
.brand-name{font-weight:800;font-size:28px;color:var(--white);letter-spacing:1px}
.nav-links{left:250px;top:46px;display:flex;gap:0;list-style:none}
.nav-links li{font-size:9px;font-weight:500;color:var(--white);width:70px}
.nav-links li:nth-child(2){width:72px}
.nav-links li:nth-child(3){width:110px}
.nav-links li:nth-child(4){width:90px}
.hero-title{left:61px;top:162px;font-size:40px;line-height:47px;font-weight:700;color:var(--white)}
.hero-title .strong{font-weight:800}
.hero-title .underline{position:absolute;left:30px;top:46px;width:200px;height:10px}
.hero-lede{left:61px;top:288px;width:470px;font-size:20px;line-height:25px;color:var(--white)}

.inquiry{left:145px;top:403px;width:374px;height:375px;background:var(--panel);border-radius:30px}
.field{position:absolute;background:var(--white);border-radius:16px;font-size:11px;font-weight:600;padding:8px 0 0 24px;color:var(--ink)}
.f-name{left:18px;top:34px;width:336px;height:31px}
.f-email{left:18px;top:82px;width:164px;height:31px}
.f-phone{left:192px;top:82px;width:162px;height:31px}
.f-msg{left:18px;top:182px;width:336px;height:126px;border-radius:18px;padding-top:10px}
.checks{position:absolute;left:18px;top:138px;display:flex;gap:22px;font-size:11px;color:var(--white);align-items:center}
.checks span{display:flex;align-items:center;gap:10px}
.checks i{display:inline-block;width:22px;height:22px;background:var(--white);border-radius:5px}
.send{position:absolute;left:124px;top:331px;width:126px;height:22px;border-radius:11px;background:var(--gold);color:var(--white);font-size:11px;text-align:center;line-height:22px}

/* experience */
.exp-title{left:184px;top:968px;font-size:34px;font-weight:700;color:var(--ink)}
.exp-title .gold{color:var(--gold)}
.exp-rule{left:265px;top:1016px;width:170px;height:8px}
.exp-copy{left:188px;top:1042px;width:400px;font-size:14px;line-height:17px;color:var(--ink)}
.exp-copy p+p{margin-top:17px}
.exp-frame{left:694px;top:979px;width:316px;height:315px;background:var(--gold);border-radius:28px}
.exp-photo{position:absolute;left:14px;top:14px;width:288px;height:287px;border-radius:20px;background:linear-gradient(135deg,#c9c2b6,#7d6a5b 55%,#3a2e2a)}

/* services */
.sec-title{width:1200px;left:0;text-align:center;font-size:34px;font-weight:700;color:var(--ink)}
.sec-rule{left:540px;width:120px;height:8px}
.svc{width:225px;text-align:center}
.svc-photo{width:222px;height:222px;border-radius:28px;margin:0 auto}
.svc-name{margin-top:14px;font-size:15px;font-weight:600;color:var(--gold)}
.svc-box{margin-top:8px;height:146px;border:2px solid var(--gold);border-radius:16px;color:var(--white);font-size:12.5px;line-height:15.5px;padding:16px 12px 0}
.svc-btn{margin:26px auto 0;width:138px;height:24px;border-radius:12px;background:var(--gold);color:var(--white);font-size:11px;line-height:24px}

/* stats */
.stats-bg{left:0;top:2097px;width:1200px;height:500px;background:var(--dark)}
.stat-rule{top:2187px;width:4px;height:273px;background:var(--white)}
.stat{top:2230px;text-align:center;color:var(--white);font-family:"Oswald",sans-serif}
.stat b{display:block;font-size:88px;line-height:90px;font-weight:600}
.stat span{display:block;font-size:28px;line-height:35px}

/* upcoming */
.sale{width:230px}
.sale-photo{width:222px;height:222px;border-radius:26px}
.sale-name{margin-top:16px;font-size:28px;font-weight:500;color:var(--purple);padding-left:10px}
.sale-where{display:flex;gap:10px;margin-top:2px;font-size:17px;line-height:20px;color:var(--grey);padding-left:10px}
.sale-where svg{flex:none;margin-top:2px}
.sale-date{margin:14px 0 0 26px;width:156px;height:22px;background:var(--purple);color:var(--white);font-size:16px;text-align:center;line-height:22px}

/* footer */
.footer-bg{left:0;top:3380px;width:1200px;height:1000px;background:var(--dark)}
.footer-brand{left:160px;top:3660px;display:flex;align-items:center;gap:14px}
.footer-brand .brand-mark{width:56px;height:56px;border-width:4px}
.footer-brand .brand-name{font-size:56px}
.footer-about{left:119px;top:3828px;width:330px;font-size:20px;line-height:25px;color:var(--white)}
.footer-divider{left:598px;top:3608px;width:3px;height:700px;background:var(--white)}
.footer-head{left:114px;top:3954px;font-size:24px;font-weight:600;color:var(--gold)}
.footer-list{list-style:none;font-size:20px;line-height:35.5px;color:var(--white)}
.footer-vr{left:265px;top:3946px;width:2px;height:208px;background:var(--gold)}
.disclaimer{left:696px;top:3845px;width:410px;font-size:19px;line-height:23.5px;color:var(--white)}
.disclaimer b{font-weight:700}
.copyright{left:696px;top:4150px;font-size:16px;color:var(--white)}
.social{top:4216px;width:62px;height:62px;border-radius:50%;background:var(--gold)}
.footer-strip{left:0;top:4357px;width:1200px;height:30px;background:var(--purple)}
</style>
</head>
<body>

<!-- HERO -->
<div class="abs hero-photo" role="img" aria-label="Photo of a grey two-storey suburban house with a green lawn and trees"></div>
<div class="abs hero-panel"></div>

<header class="abs site-nav">
  <div class="abs brand"><span class="brand-mark"></span><span class="brand-name">BHES</span></div>
  <ul class="abs nav-links">
    <li>Home</li><li>Services</li><li>Upcoming Sales</li><li>About Us</li><li>FAQs</li><li>Resources</li>
  </ul>
</header>

<h1 class="abs hero-title"><span class="strong">Professional</span> Solutions<br>for Every Phase
  <svg class="underline" viewBox="0 0 200 10"><path d="M2 8 Q100 -2 198 5" stroke="#c9962e" stroke-width="3" fill="none"/></svg>
</h1>
<p class="abs hero-lede">With 20 years of experience in the Nashville Market, let us help you unlock the reasures of the Nashville Estate arena.</p>

<svg class="band" style="top:600px;height:340px" viewBox="0 0 1200 340" preserveAspectRatio="none">
  <path d="M0 215 Q560 360 1200 100 L1200 340 L0 340 Z" fill="#ffffff"/>
  <path d="M0 180 Q600 300 1200 20 L1200 55 Q600 330 0 200 Z" fill="#5a27a5"/>
  <path d="M0 205 Q560 345 1200 90 L1200 125 Q560 390 0 250 Z" fill="#c9962e"/>
</svg>

<form class="abs inquiry">
  <div class="field f-name">Name</div>
  <div class="field f-email">Email</div>
  <div class="field f-phone">Phone No.</div>
  <div class="checks"><span><i></i>Estate Sales</span><span><i></i>Cleanouts</span><span><i></i>Appraisals</span></div>
  <div class="field f-msg">Message</div>
  <div class="send">Send</div>
</form>

<!-- EXPERIENCE -->
<svg class="band" style="top:980px;height:400px" viewBox="0 0 1200 400" preserveAspectRatio="none">
  <path d="M1020 95 Q1100 40 1200 20 L1200 55 Q1100 75 1020 130 Z" fill="#5a27a5"/>
  <path d="M1020 150 Q1100 85 1200 68 L1200 110 Q1110 125 1020 180 Z" fill="#c9962e"/>
  <path d="M0 300 Q400 360 700 245 L700 270 Q400 385 0 330 Z" fill="#c9962e"/>
  <path d="M0 320 Q400 390 700 270 L700 300 Q400 420 0 360 Z" fill="#5a27a5"/>
  <path d="M1200 340 Q1130 360 1110 470 Q1150 400 1200 395 Z" fill="#5a27a5"/>
</svg>
<h2 class="abs exp-title"><span class="gold">Experience</span> our Difference</h2>
<svg class="abs exp-rule" viewBox="0 0 170 8"><path d="M2 6 Q85 -1 168 5" stroke="#5a27a5" stroke-width="3" fill="none"/></svg>
<div class="abs exp-copy">
  <p>With a wealth of experience and expertise, our estate sale team can assist you from start to finish with every phase of the Nashville Estate Sale liquidation process.</p>
  <p>Whether you're downsizing, relocating, or settling an estate, our dedicated team is committed to providing professional and personalized solutions tailored to your unique needs. Let us help you navigate the complexities of estate liquidation with care, integrity, and efficiency."</p>
</div>
<div class="abs exp-frame"><div class="exp-photo" role="img" aria-label="Photo of an agent handing house keys to a client in a bright hallway"></div></div>

<!-- SERVICES -->
<svg class="band" style="top:1560px;height:540px" viewBox="0 0 1200 540" preserveAspectRatio="none">
  <defs><linearGradient id="svcbg" x1="0" y1="0" x2="0" y2="1"><stop offset="0" stop-color="#5a27a5"/><stop offset="1" stop-color="#5330a0"/></linearGradient></defs>
  <path d="M0 115 Q600 0 1200 115 L1200 540 L0 540 Z" fill="url(#svcbg)"/>
</svg>
<h2 class="abs sec-title" style="top:1390px">Services</h2>
<svg class="abs sec-rule" style="top:1438px" viewBox="0 0 120 8"><path d="M2 6 Q60 -1 118 5" stroke="#c9962e" stroke-width="3" fill="none"/></svg>

<div class="abs svc" style="left:189px;top:1486px">
  <div class="svc-photo" role="img" aria-label="Photo of a large white estate home with a stone driveway" style="background:linear-gradient(180deg,#9fb3c9,#e8e8ea 50%,#8a8d8f)"></div>
  <div class="svc-name">Estate Sales</div>
  <div class="svc-box">Offering comprehensive estate liquidation services. We handle everything from inventory assessment to hosting the sale event, maximizing value while minimizing stress.</div>
  <div class="svc-btn">Learn More</div>
</div>
<div class="abs svc" style="left:487px;top:1486px">
  <div class="svc-photo" role="img" aria-label="Photo of a family packing cardboard boxes in an empty room" style="background:linear-gradient(180deg,#e6e2dc,#d9cfc4 55%,#b88a5c)"></div>
  <div class="svc-name" style="margin-top:18px">Cleanouts</div>
  <div class="svc-box" style="margin-top:6px">Our hassle-free cleanout service swiftly clears properties. Whether decluttering, prepping for sale, or managing foreclosures, we ensure efficient, discreet removal.</div>
  <div class="svc-btn">Learn More</div>
</div>
<div class="abs svc" style="left:787px;top:1486px">
  <div class="svc-photo" role="img" aria-label="Photo of an appraiser with a clipboard talking to a couple" style="background:linear-gradient(135deg,#d8d8d8,#8fa8c4 50%,#3c3c3c)"></div>
  <div class="svc-name" style="margin-top:18px">Appraisals</div>
  <div class="svc-box" style="margin-top:6px">Trust our expert appraisals for accurate valuations. From antiques to art, we provide fair market assessments for estate planning, insurance, or resale purposes.</div>
  <div class="svc-btn">Learn More</div>
</div>

<!-- STATS -->
<div class="abs stats-bg"></div>
<div class="abs stat-rule" style="left:185px"></div>
<div class="abs stat-rule" style="left:458px"></div>
<div class="abs stat-rule" style="left:726px"></div>
<div class="abs stat-rule" style="left:1009px"></div>
<div class="abs stat" style="left:230px;width:220px"><b>20+</b><span>Years of<br>Experience</span></div>
<div class="abs stat" style="left:480px;width:230px"><b>$50M</b><span>In Sales</span></div>
<div class="abs stat" style="left:758px;width:220px"><b>5+</b><span>Satisfied<br>Customers</span></div>

<!-- UPCOMING SALES -->
<svg class="band" style="top:2500px;height:380px" viewBox="0 0 1200 380" preserveAspectRatio="none">
  <path d="M0 200 Q560 -10 1200 110 L1200 380 L0 380 Z" fill="#ffffff"/>
  <path d="M0 150 Q560 -30 1200 60 L1200 95 Q560 10 0 185 Z" fill="#c9962e"/>
  <path d="M0 190 Q560 20 1200 100 L1200 120 Q560 50 0 205 Z" fill="#5a27a5"/>
  <path d="M0 240 Q60 260 72 255 Q50 330 0 345 Z" fill="#5a27a5"/>
  <path d="M0 205 Q40 215 70 250 Q30 230 0 235 Z" fill="#c9962e"/>
</svg>
<h2 class="abs sec-title" style="top:2724px">Upcoming Sales</h2>
<svg class="abs sec-rule" style="top:2772px" viewBox="0 0 120 8"><path d="M2 6 Q60 -1 118 5" stroke="#5a27a5" stroke-width="3" fill="none"/></svg>

<div class="abs sale" style="left:191px;top:2851px">
  <div class="sale-photo" role="img" aria-label="Photo of an outdoor yard sale in front of a shingled house" style="background:linear-gradient(180deg,#8a6a4e,#a58e74 50%,#6d7a52)"></div>
  <div class="sale-name">Lorem ipsum</div>
  <div class="sale-where"><svg width="26" height="34" viewBox="0 0 26 34"><path d="M13 1C6 1 1 6 1 13c0 9 12 20 12 20s12-11 12-20C25 6 20 1 13 1z" fill="#c9962e"/><circle cx="13" cy="13" r="5" fill="#fff"/></svg><span>Lorem ipsum dolor<br>sit amet.</span></div>
  <div class="sale-date">March 01 - 02</div>
</div>
<div class="abs sale" style="left:489px;top:2851px">
  <div class="sale-photo" role="img" aria-label="Photo of vintage chairs and a blue dresser for sale" style="background:linear-gradient(180deg,#5d7a8a,#b89a6e 55%,#7a5a3e)"></div>
  <div class="sale-name">Lorem ipsum</div>
  <div class="sale-where"><svg width="26" height="34" viewBox="0 0 26 34"><path d="M13 1C6 1 1 6 1 13c0 9 12 20 12 20s12-11 12-20C25 6 20 1 13 1z" fill="#c9962e"/><circle cx="13" cy="13" r="5" fill="#fff"/></svg><span>Lorem ipsum dolor<br>sit amet.</span></div>
  <div class="sale-date">March 01 - 02</div>
</div>
<div class="abs sale" style="left:789px;top:2851px">
  <div class="sale-photo" role="img" aria-label="Photo of a garage sale in an open garage with a sandy driveway" style="background:linear-gradient(180deg,#cfd8dc,#c9b79a 50%,#d8c6a4)"></div>
  <div class="sale-name">Lorem ipsum</div>
  <div class="sale-where"><svg width="26" height="34" viewBox="0 0 26 34"><path d="M13 1C6 1 1 6 1 13c0 9 12 20 12 20s12-11 12-20C25 6 20 1 13 1z" fill="#c9962e"/><circle cx="13" cy="13" r="5" fill="#fff"/></svg><span>Lorem ipsum dolor<br>sit amet.</span></div>
  <div class="sale-date">March 01 - 02</div>
</div>

<!-- FOOTER -->
<div class="abs footer-bg"></div>
<svg class="band" style="top:3320px;height:240px" viewBox="0 0 1200 240" preserveAspectRatio="none">
  <path d="M0 0 L1200 0 L1200 60 Q600 260 0 40 Z" fill="#ffffff"/>
  <path d="M0 20 Q600 200 1200 35 L1200 55 Q600 230 0 45 Z" fill="#5a27a5"/>
  <path d="M0 60 Q600 240 1200 60 L1200 85 Q600 270 0 95 Z" fill="#c9962e"/>
</svg>

<div class="abs footer-brand"><span class="brand-mark"></span><span class="brand-name">BHES</span></div>
<p class="abs footer-about">Lorem ipsum dolor sit amet, consectetuer Lorem ipsum dolor sit amet,.</p>
<div class="abs footer-divider"></div>

<h3 class="abs footer-head">Services</h3>
<ul class="abs footer-list" style="left:119px;top:4003px"><li>Estate Sales</li><li>Cleanouts</li><li>Appraisals</li></ul>
<div class="abs footer-vr"></div>
<ul class="abs footer-list" style="left:300px;top:3946px"><li>Services</li><li>Upcoming Sales</li><li>About Us</li><li>FAQs</li><li>Resources</li></ul>

<p class="abs disclaimer"><b>Disclaimer:</b> Lorem ipsum dolor sit amet, consectetuer adipiscing elit, sed diam nonummy nibh euismod tincidunt ut laoreet dolore magna aliquam erat volutpat. Ut wisi enim ad minim veniam, quis nostrud exerci tation ullamcorper suscipit lobortis nisl ut aliquip ex ea commodo consequat. Duis autem vel eum iriure dolor in hendrerit in vulputate velit esse molestie consequat, vel illum dolore eu feugiat nulla facilisis at vero eros et accumsan et iusto odio.</p>
<p class="abs copyright">© Bright Haven Estate Sales. All Right Reserved.</p>

<div class="abs social" style="left:117px" role="img" aria-label="Social link"></div>
<div class="abs social" style="left:199px" role="img" aria-label="Social link"></div>
<div class="abs social" style="left:279px" role="img" aria-label="Social link"></div>
<div class="abs social" style="left:359px" role="img" aria-label="Social link"></div>
<div class="abs social" style="left:436px" role="img" aria-label="Social link"></div>

<div class="abs footer-strip"></div>
</body>
</html>
```